Business Card Design and a letter head logo

50/50 share milker dairy farmer of 400 cows with a silage and haymaking sideline business
15 years farming currently looking for new opportunities within the dairy farming sector. trying to put together a portfolio to get another 50/50 share milking job aswell

Industry/Entity Type

Farming

Contact Information for Business Card

Brindle Farming LTD
Corwin & Lisette Pargeter
263 Kellow Ridge Highway
RD4 Tepuhina 0382
Whangarei
pargeter.corwin@fernmail.example.nz
0274381926
(09) 5817342

```html
<!DOCTYPE html>
<html lang="en">
<head>
<meta charset="utf-8">
<title>Brindle Farming LTD – Business Card</title>
<link href="https://fonts.googleapis.com/css2?family=Arimo:wght@400;700&display=swap" rel="stylesheet">
<style>
  :root {
    --page: #e9e6e1;
    --card-dark: #050505;
    --card-glow: #2a2a2a;
    --green: #7ab648;
    --tan: #c49a6c;
    --white: #ffffff;
  }
  * { box-sizing: border-box; margin: 0; padding: 0; }
  html, body {
    width: 1200px; height: 1000px; overflow: hidden;
    background: var(--page);
    font-family: "Arimo", Arial, sans-serif;
  }
  .business-card {
    position: absolute; left: 100px; top: 214px;
    width: 1000px; height: 572px;
    background: radial-gradient(ellipse at 50% 35%, var(--card-glow) 0%, var(--card-dark) 65%);
    overflow: hidden;
    box-shadow: 0 12px 30px rgba(0,0,0,.25);
  }
  .card-bands { position: absolute; inset: 0; width: 100%; height: 100%; }
  .brand {
    position: absolute; left: 70px; top: 140px;
    display: flex; align-items: center; gap: 16px;
  }
  .brand-mark {
    width: 50px; height: 50px; border-radius: 50%;
    background: var(--green);
  }
  .brand-name {
    color: var(--green); font-weight: 400;
    font-size: 38px; letter-spacing: 1px; line-height: 1.1;
    white-space: nowrap;
  }
  .address {
    position: absolute; left: 590px; top: 84px;
    display: flex; gap: 12px; align-items: flex-start;
    color: var(--white); font-size: 21px; line-height: 1.25;
    white-space: nowrap;
  }
  .icon { flex: none; width: 26px; height: 26px; }
  .holders {
    position: absolute; right: 460px; top: 282px;
    color: var(--white); font-size: 40px; line-height: 1.2;
    text-align: left; white-space: nowrap;
  }
  .divider {
    position: absolute; left: 562px; top: 276px;
    width: 2px; height: 120px; background: var(--tan);
  }
  .contact-list {
    position: absolute; left: 580px; top: 272px;
    list-style: none; color: var(--white);
  }
  .contact-list li {
    display: flex; align-items: center; gap: 10px;
    font-size: 22px; height: 40px; white-space: nowrap;
  }
  .contact-list .email { font-size: 18px; }
</style>
</head>
<body>
  <article class="business-card">
    <svg class="card-bands" viewBox="0 0 1000 572" preserveAspectRatio="none" aria-hidden="true">
      <polygon points="0,545 505,470 468,545" fill="var(--tan)"/>
      <polygon points="530,468 1000,400 1000,500 492,545" fill="var(--green)"/>
      <rect x="0" y="556" width="1000" height="16" fill="var(--tan)"/>
    </svg>

    <div class="brand">
      <span class="brand-mark"></span>
      <span class="brand-name">Brindle Farming LTD</span>
    </div>

    <div class="address">
      <svg class="icon" viewBox="0 0 26 26" aria-hidden="true">
        <circle cx="13" cy="13" r="13" fill="var(--green)"/>
        <path d="M13 5.5a5 5 0 0 0-5 5c0 3.8 5 9.5 5 9.5s5-5.7 5-9.5a5 5 0 0 0-5-5z" fill="var(--card-dark)"/>
        <circle cx="13" cy="10.5" r="1.9" fill="var(--green)"/>
      </svg>
      <p>263 Kellow Ridge Highway RD4<br>Tepuhina 0382 Whangarei</p>
    </div>

    <div class="holders">
      <p>Corwin Pargeter</p>
      <p>Lisette Pargeter</p>
    </div>

    <span class="divider"></span>

    <ul class="contact-list">
      <li>
        <svg class="icon" viewBox="0 0 26 26" aria-hidden="true">
          <circle cx="13" cy="13" r="13" fill="var(--green)"/>
          <path d="M9 7l3 3-1.6 1.8c.9 1.8 2.2 3.1 4 4L16 14.2l3 3-1.8 2C12 19 7 14 6.8 8.8z" fill="var(--card-dark)"/>
        </svg>
        <span>(09) 5817342</span>
      </li>
      <li>
        <svg class="icon" viewBox="0 0 26 26" aria-hidden="true">
          <circle cx="13" cy="13" r="13" fill="var(--green)"/>
          <rect x="9" y="6" width="8" height="14" rx="1.5" fill="var(--card-dark)"/>
          <rect x="10.5" y="8" width="5" height="8" fill="var(--green)"/>
        </svg>
        <span>0274381926</span>
      </li>
      <li class="email">
        <svg class="icon" viewBox="0 0 26 26" aria-hidden="true">
          <circle cx="13" cy="13" r="13" fill="var(--green)"/>
          <rect x="6.5" y="8.5" width="13" height="9" fill="var(--card-dark)"/>
          <path d="M6.5 8.5l6.5 5 6.5-5" fill="none" stroke="var(--green)" stroke-width="1.3"/>
        </svg>
        <span>pargeter.corwin@fernmail.example.nz</span>
      </li>
    </ul>
  </article>
</body>
</html>
```